Velvet Crypt Mixtape Podcast Design

My audio drama podcast is a funny horror story with romantic elements called Velvet Crypt Mixtape.
I'm looking for a colorful design featuring the title and letting the viewer know this is a horror show.
The title needs to be clearly visible even in thumbnail size.

```html
<!DOCTYPE html>
<html lang="en">
<head>
<meta charset="UTF-8">
<title>Velvet Crypt Mixtape – Podcast Cover</title>
<link href="https://fonts.googleapis.com/css2?family=Creepster&display=swap" rel="stylesheet">
<style>
  :root {
    --magenta: #c8188a;
    --rose: #e3185a;
    --red: #f32224;
    --blood-orange: #fa3d10;
    --orange: #f98f0a;
    --yellow: #e6d80a;
    --lime: #9ef00a;
    --green: #44ff00;
    --title-orange: #eead48;
    --title-white: #ffffff;
    --shadow-red: #7a0d1c;
    --ink: #0b0a0c;
    --lip-red: #a5200f;
    --tooth-gold: #f6c81a;
    --foliage: #1c3a06;
  }
  * { margin: 0; padding: 0; box-sizing: border-box; }
  html, body {
    width: 1200px;
    height: 1200px;
    overflow: hidden;
    background: #e8e8e8;
  }
  .cover {
    position: relative;
    width: 1200px;
    height: 1200px;
    overflow: hidden;
    background: linear-gradient(180deg,
      var(--magenta) 0%,
      var(--rose) 22%,
      var(--red) 38%,
      var(--blood-orange) 50%,
      var(--orange) 63%,
      var(--yellow) 77%,
      var(--lime) 88%,
      var(--green) 100%);
    font-family: 'Creepster', fantasy;
  }
  .title {
    position: absolute;
    top: 58px;
    left: 0;
    width: 100%;
    text-align: center;
    line-height: 1;
  }
  .title span { display: block; }
  .title-top, .title-bottom {
    color: var(--title-orange);
    font-size: 150px;
    letter-spacing: 6px;
    text-shadow: 3px 4px 4px rgba(90, 10, 20, 0.55);
  }
  .title-main {
    color: var(--title-white);
    font-size: 200px;
    letter-spacing: 14px;
    margin: 4px 0 6px;
    text-shadow: 4px 6px 6px var(--shadow-red);
  }
  .mouth-art {
    position: absolute;
    left: 317px;
    top: 614px;
    width: 641px;
    height: 359px;
    border-radius: 48% 52% 46% 54% / 40% 45% 58% 60%;
    transform: rotate(-6deg);
    background: radial-gradient(ellipse at 50% 52%,
      var(--tooth-gold) 0%, var(--tooth-gold) 38%,
      var(--ink) 52%, var(--lip-red) 68%, #5a0f07 100%);
  }
  .decor {
    position: absolute;
    left: 0;
    top: 0;
  }
  .meadow-art {
    position: absolute;
    left: 0;
    top: 940px;
    width: 1200px;
    height: 253px;
    background: linear-gradient(180deg, rgba(28, 58, 6, 0) 0%, rgba(28, 58, 6, 0.55) 100%);
  }
  .ground-line {
    position: absolute;
    left: 0;
    top: 1193px;
    width: 1200px;
    height: 7px;
    background: var(--ink);
  }
</style>
</head>
<body>
  <main class="cover">
    <h1 class="title">
      <span class="title-top">VELVET</span>
      <span class="title-main">CRYPT</span>
      <span class="title-bottom">MIXTAPE</span>
    </h1>

    <div class="mouth-art" role="img" aria-label="Illustration of grinning red lips with gold teeth"></div>

    <svg class="decor" width="1200" height="1200" viewBox="0 0 1200 1200" aria-hidden="true">
      <defs>
        <path id="heart" d="M0,-18 C-6,-34 -36,-32 -36,-8 C-36,10 -14,26 0,42 C14,26 36,10 36,-8 C36,-32 6,-34 0,-18 Z"/>
        <path id="drop" d="M0,-20 C6,-8 10,0 10,7 C10,13 5,18 0,18 C-5,18 -10,13 -10,7 C-10,0 -6,-8 0,-20 Z"/>
      </defs>
      <g fill="var(--ink)">
        <use href="#heart" transform="translate(921,552) rotate(-12) scale(1.02)"/>
        <use href="#heart" transform="translate(960,616) rotate(10) scale(0.72)"/>
        <use href="#heart" transform="translate(252,770) rotate(-10) scale(1.02)"/>
        <use href="#heart" transform="translate(290,838) rotate(12) scale(0.74)"/>
        <use href="#drop" transform="translate(996,748) scale(1)"/>
        <use href="#drop" transform="translate(982,812) scale(0.9)"/>
        <use href="#drop" transform="translate(330,942) scale(1)"/>
      </g>
    </svg>

    <div class="meadow-art" role="img" aria-label="Illustration of black sprouting plants and green flowers along the ground"></div>
    <div class="ground-line"></div>
  </main>
</body>
</html>
```